Halloway Crest Backers Guild business cards

Create a single-sided business card for the Halloway Crest Backers Guild based on the attached logo.
The additional data fields include Name, Title, Email, Phone, and website.
Please use the following as sample data:
Name: Dean Varrow
Title: Co-Founder / Investor
Email: deanvarrow@mailtern.net
Phone: 555-314-2706
Website: www.hcbackersguild.com

Target Market(s)

Start ups, entrepreneurs, venture capitalists

Industry/Entity Type

Investment

Contact Information for Business Card

Professional business card. Technology company.

Font styles to use
Serif
Sans Serif

Requirements
Must have
• Include the HCBG logo (attached)
• Name
• Title
• Email
• Phone
• Website
Should not have
• Cute, cartoony

```html
<!DOCTYPE html>
<html lang="en">
<head>
<meta charset="utf-8">
<title>Halloway Crest Backers Guild – Business Card</title>
<link href="https://fonts.googleapis.com/css2?family=Open+Sans:wght@400;600;700&display=swap" rel="stylesheet">
<style>
  :root {
    --green: #0c9a4f;
    --charcoal: #404043;
    --ink: #2e2e30;
    --paper: #ffffff;
    --backdrop: #e9e7e4;
  }
  * { margin: 0; padding: 0; box-sizing: border-box; }
  html, body {
    width: 1200px;
    height: 1000px;
    overflow: hidden;
    background: var(--backdrop);
    font-family: "Open Sans", Arial, sans-serif;
  }
  .business-card {
    position: absolute;
    left: 100px;
    top: 201px;
    width: 1000px;
    height: 597px;
    background: var(--paper);
    box-shadow: 0 4px 14px rgba(0,0,0,0.12);
    overflow: hidden;
  }
  .brand {
    position: absolute;
    left: 48px;
    top: 63px;
    height: 146px;
    display: flex;
    align-items: center;
  }
  .brand-mark {
    width: 40px;
    height: 40px;
    background: var(--green);
    margin-right: 30px;
  }
  .brand-divider {
    width: 2px;
    height: 146px;
    background: var(--green);
    margin-right: 20px;
  }
  .brand-name {
    color: var(--green);
    font-weight: 600;
    font-size: 44px;
    line-height: 50px;
  }
  .person {
    position: absolute;
    left: 48px;
    top: 290px;
  }
  .person-name {
    color: var(--green);
    font-weight: 600;
    font-size: 39px;
    line-height: 44px;
  }
  .person-title {
    color: var(--ink);
    font-size: 24px;
    line-height: 32px;
  }
  .rule {
    position: absolute;
    left: 48px;
    top: 371px;
    width: 903px;
    height: 3px;
    background: var(--ink);
  }
  .contact-list {
    position: absolute;
    left: 48px;
    top: 412px;
    list-style: none;
  }
  .contact-item {
    display: flex;
    align-items: center;
    height: 36px;
    color: var(--ink);
    font-size: 24px;
  }
  .contact-icon {
    width: 22px;
    height: 22px;
    margin-right: 11px;
    fill: var(--green);
  }
  .address {
    position: absolute;
    right: 48px;
    top: 448px;
    text-align: right;
    color: var(--ink);
    font-size: 24px;
    line-height: 36px;
    font-style: normal;
  }
  .band {
    position: absolute;
    bottom: 0;
    height: 47px;
  }
  .band-dark { left: 0; width: 568px; background: var(--charcoal); }
  .band-green { left: 576px; right: 0; background: var(--green); }
</style>
</head>
<body>
  <article class="business-card">
    <header class="brand">
      <div class="brand-mark"></div>
      <div class="brand-divider"></div>
      <div class="brand-name">Halloway Crest<br>Backers Guild</div>
    </header>

    <section class="person">
      <h1 class="person-name">DEAN VARROW</h1>
      <p class="person-title">Co-Founder / Investor</p>
    </section>

    <div class="rule"></div>

    <ul class="contact-list">
      <li class="contact-item">
        <svg class="contact-icon" viewBox="0 0 24 24" aria-hidden="true"><path d="M3 9c0-3 4-5 9-5s9 2 9 5v2h-5V9c-1-1-7-1-8 0v2H3zM6 12h12l2 7H4z"/><circle cx="12" cy="15.5" r="2" fill="#fff"/></svg>
        555-314-2706
      </li>
      <li class="contact-item">
        <svg class="contact-icon" viewBox="0 0 24 24" aria-hidden="true"><path d="M2 5h20v14H2z"/><path d="M2 5l10 8 10-8" fill="none" stroke="#fff" stroke-width="2"/></svg>
        deanvarrow@mailtern.net
      </li>
      <li class="contact-item">
        <svg class="contact-icon" viewBox="0 0 24 24" aria-hidden="true"><circle cx="11" cy="11" r="9"/><path d="M2 11h18M11 2c-4 5-4 13 0 18M11 2c4 5 4 13 0 18" fill="none" stroke="#fff" stroke-width="1.4"/><path d="M14 14l8 3-3 1-1 3z" stroke="#fff" stroke-width="1"/></svg>
        www.hcbackersguild.com
      </li>
    </ul>

    <address class="address">
      Level 29, 7 Brennick Tower<br>
      Sydney, 20, New South Wales
    </address>

    <div class="band band-dark"></div>
    <div class="band band-green"></div>
  </article>
</body>
</html>
```